Brindle Capital and Investments

Create a simple business card design using the logos attached. Make it similar but not exact to the reference photo. Brand guidelines are also included.

```html
<!DOCTYPE html>
<html lang="en">
<head>
<meta charset="utf-8">
<title>Brindle Capital – Business Card</title>
<link href="https://fonts.googleapis.com/css2?family=Open+Sans:wght@400;600;700;800&display=swap" rel="stylesheet">
<style>
  :root {
    --backdrop: #cfcdce;
    --navy: #0b1437;
    --rust: #9a4a22;
    --ink: #5b5b5b;
    --paper: #ffffff;
  }
  * { margin: 0; padding: 0; box-sizing: border-box; }
  html, body { width: 956px; height: 1200px; overflow: hidden; }
  body {
    background: var(--backdrop);
    font-family: "Open Sans", Arial, sans-serif;
    position: relative;
  }
  .card {
    position: absolute;
    left: 74px;
    width: 808px;
    height: 462px;
    overflow: hidden;
    box-shadow: 2px 3px 5px rgba(0,0,0,0.35);
  }
  .card--front { top: 115px; background: var(--paper); }
  .card--back { top: 624px; background: var(--navy); }

  .wordmark {
    position: absolute;
    text-align: center;
    font-weight: 800;
    line-height: 1;
  }
  .card--front .wordmark { left: 90px; width: 280px; top: 190px; color: var(--navy); }
  .card--back .wordmark { left: 204px; width: 400px; top: 200px; color: var(--paper); }
  .wordmark__main { display: block; font-size: 52px; letter-spacing: 6px; margin-right: -6px; }
  .wordmark__sub { display: block; font-size: 24px; letter-spacing: 12px; margin-right: -12px; margin-top: 14px; }
  .card--back .wordmark__main { font-size: 62px; letter-spacing: 8px; margin-right: -8px; }
  .card--back .wordmark__sub { font-size: 30px; letter-spacing: 15px; margin-right: -15px; margin-top: 18px; }

  .divider {
    position: absolute;
    left: 403px;
    top: 113px;
    width: 2px;
    height: 236px;
    background: #6c6c6c;
  }
  .contact { position: absolute; left: 438px; top: 104px; color: var(--ink); }
  .contact__name { font-size: 30px; font-weight: 700; color: var(--rust); line-height: 1.15; letter-spacing: 0.2px; }
  .contact__title { font-size: 24px; line-height: 1.2; margin-left: 2px; }
  .contact__address { font-size: 24px; line-height: 29px; margin-top: 16px; }
  .contact__lines { list-style: none; margin-top: 15px; font-size: 24px; line-height: 29px; }
  .contact__lines li { display: flex; align-items: center; gap: 6px; }
  .contact__lines svg { width: 17px; height: 17px; fill: var(--rust); flex: none; }

  .base-band {
    position: absolute;
    left: 0; bottom: 0;
    width: 100%;
    height: 44px;
    background: var(--navy);
  }
  .base-rule {
    position: absolute;
    left: 0; bottom: 52px;
    width: 100%;
    height: 6px;
    background: var(--rust);
  }

  .web {
    position: absolute;
    left: 0; width: 808px;
    top: 392px;
    text-align: center;
    font-size: 22px;
    letter-spacing: 6px;
    color: var(--paper);
  }
  .web__name { color: var(--rust); font-weight: 700; }
</style>
</head>
<body>

<section class="card card--front">
  <div class="wordmark">
    <span class="wordmark__main">BRINDLE</span>
    <span class="wordmark__sub">CAPITAL</span>
  </div>

  <div class="divider"></div>

  <div class="contact">
    <h1 class="contact__name">JONATHAN SMITH</h1>
    <p class="contact__title">Managing Director</p>
    <p class="contact__address">Your Address, City<br>State, Zip 0000</p>
    <ul class="contact__lines">
      <li>
        <svg viewBox="0 0 20 20" aria-hidden="true"><path d="M2 7c0-2 3-4 8-4s8 2 8 4v1h-4V6.5c-1-.6-2.4-.9-4-.9s-3 .3-4 .9V8H2z"/><path d="M4 10l2-2h8l2 2v7H4z"/></svg>
        <span>044-123 456 789</span>
      </li>
      <li>
        <svg viewBox="0 0 20 20" aria-hidden="true"><path d="M10 2l8 6v10H2V8z"/><path d="M3 17l7-5 7 5z" fill="#fff"/></svg>
        <span>info@webname.com</span>
      </li>
      <li>
        <svg viewBox="0 0 20 20" aria-hidden="true"><circle cx="10" cy="10" r="8.5"/><path d="M6 5c2 0 3 2 2 3s-3 1-3 3 2 2 2 4c-2-1-4-3-4-5s1-4 3-5zm7 3c2 0 3 2 2 4s-2 2-3 1 0-3 1-5z" fill="#fff"/></svg>
        <span>www.websitename.com</span>
      </li>
    </ul>
  </div>

  <div class="base-rule"></div>
  <div class="base-band"></div>
</section>

<section class="card card--back">
  <div class="wordmark">
    <span class="wordmark__main">BRINDLE</span>
    <span class="wordmark__sub">CAPITAL</span>
  </div>
  <p class="web">www.<span class="web__name">websitename</span>.com</p>
</section>

</body>
</html>
```